Brand New Solar Energy Business Needs a Flyer Design

We need an A5 double sided flyer for a new company in South Australia called Dorrit & Vale. We install home solar power systems and try to focus on quality of product and install.We also offer solar system servicing for existing systems which includes maintenance, cleaning and safety checks. Our web address is www.dorritandvale.com.au
We would like to see a design that's fresh and stands out in the mail box.
We feel the final design should communicate saving money on your electricity bills, local, quality and safety.
Target Market(s)
Home owners
Industry/Entity Type
Safety
Requirements
Must have
- A reference to our web site www.dorritandvale.com.au
A telephone number 0491638274

```html
<!DOCTYPE html>
<html lang="en">
<head>
<meta charset="utf-8">
<title>Dorrit &amp; Vale – Residential Solar Flyer</title>
<link href="https://fonts.googleapis.com/css2?family=Arimo:wght@400;700&display=swap" rel="stylesheet">
<style>
  :root {
    --brand-blue: #1d5c9f;
    --brand-blue-deep: #174d88;
    --accent-cyan: #3bb3e6;
    --accent-light: #bfe4f6;
    --text-white: #ffffff;
    --paper: #ffffff;
    --logo-green: #3a9a3c;
    --photo-sky: #9ccbe8;
    --photo-panel: #1f3f73;
    --photo-roof: #7a5a48;
  }
  * { box-sizing: border-box; margin: 0; padding: 0; }
  html, body { width: 845px; height: 1200px; overflow: hidden; background: var(--paper); }
  .flyer {
    position: relative;
    width: 845px;
    height: 1200px;
    font-family: "Arimo", Arial, sans-serif;
    background: var(--paper);
    overflow: hidden;
  }
  .hero-photo {
    position: absolute;
    top: 0; left: 0;
    width: 845px; height: 440px;
    background:
      linear-gradient(160deg, var(--photo-roof) 0%, var(--photo-roof) 18%, transparent 30%),
      linear-gradient(180deg, var(--photo-sky) 0%, #5d8fc4 35%, var(--photo-panel) 70%, #122c55 100%);
  }
  .content-panel {
    position: absolute;
    top: 440px; left: 0;
    width: 845px; height: 760px;
    background: var(--brand-blue);
  }
  .bottom-wave {
    position: absolute;
    left: 0; top: 960px;
    width: 845px; height: 240px;
  }
  .section-title {
    position: absolute;
    left: 70px; top: 462px;
    font-size: 35px;
    font-weight: 700;
    color: var(--text-white);
  }
  .copy-column {
    position: absolute;
    color: var(--text-white);
    font-size: 18.5px;
    line-height: 27px;
  }
  .copy-column p { margin-bottom: 27px; text-indent: 6px; }
  .copy-left { left: 70px; top: 522px; width: 345px; }
  .copy-right { left: 436px; top: 480px; width: 350px; }
  .brand-lockup {
    position: absolute;
    right: 30px; top: 1058px;
    display: flex;
    align-items: center;
    gap: 16px;
  }
  .brand-mark {
    width: 92px; height: 92px;
    border-radius: 50%;
    background: var(--logo-green);
  }
  .brand-text { display: flex; flex-direction: column; }
  .brand-name {
    font-size: 48px;
    font-weight: 700;
    color: var(--brand-blue-deep);
    line-height: 1;
  }
  .brand-tagline {
    font-size: 17px;
    color: var(--brand-blue-deep);
    margin-top: 6px;
  }
  .brand-contact {
    font-size: 16px;
    font-weight: 700;
    color: var(--brand-blue-deep);
    margin-top: 6px;
  }
</style>
</head>
<body>
<div class="flyer">
  <div class="hero-photo" role="img" aria-label="Photo of a solar installer in a cap fitting solar panels on a tiled house roof under a blue sky"></div>

  <div class="content-panel"></div>

  <svg class="bottom-wave" viewBox="0 0 845 240" preserveAspectRatio="none" aria-hidden="true">
    <path d="M0 150 C 260 170, 520 60, 845 40 L845 240 L0 240 Z" fill="var(--accent-light)"/>
    <path d="M0 170 C 260 185, 520 80, 845 60 L845 240 L0 240 Z" fill="var(--paper)"/>
    <path d="M0 150 C 260 170, 520 60, 845 40" fill="none" stroke="var(--accent-cyan)" stroke-width="6"/>
  </svg>

  <h1 class="section-title">Residential</h1>

  <div class="copy-column copy-left">
    <p>There's no disputing the environmental benefits of installing solar and with electricity costs rising again and set to rise further, there's never been a better time to install solar in your home. Dorrit &amp; Vale offers affordable premium home solar systems which we tailor to your requirments.</p>
    <p>We offer premium residential systems which are designed to slash your electricity bills, reduce your carbon footprint, pay you back quicker and installed to a very high standard. We only use premium quality products such as Norvik Germany and Heliora Solar Products. This ensures the system meets your requirements for many years to come.</p>
  </div>

  <div class="copy-column copy-right">
    <p>Your personal solar consultant will be there to answer any questions from begining to end, through the consultation phase, design stage and right through to installation completion. Our solar installers are “A” class electricians who are trained to the highest national solar standards board standards. Our installers are tasked with leaving our customers feeling knowledgeable and empowered. Dorrit &amp; Vale does not use sub contractors. When you choose your solar installer, don't forget you are dealing with electricity. Contact Dorrit &amp; Vale today to discuss solar energy for you.</p>
    <p>Locally owned in South Australia, we also service existing systems with maintenance, cleaning and safety checks.</p>
  </div>

  <div class="brand-lockup">
    <div class="brand-mark" aria-hidden="true"></div>
    <div class="brand-text">
      <span class="brand-name">Dorrit &amp; Vale</span>
      <span class="brand-tagline">Solar and Electrical Contractors</span>
      <span class="brand-contact">www.dorritandvale.com.au · 0491638274</span>
    </div>
  </div>
</div>
</body>
</html>
```